CAPPUCCINO ART FOR VELLOR BOX PACKAGING DESIGN

The product is UHT Milk in Vellor Box pagkaging.
Flavour: Mocha

The measurement is around:
- (Front & Back): 4.8 cm (Width) x 12 cm (Height)
- (Sides): 3.8 cm (Width) x 12 cm (Height)
Real measurement attached

Temporary Brand name: DUNRA.
However, you can also propose a brand name to match your design

I want the product design to have a cappuccino art.
The shape/ art could be anything: leafs, animal picture, or other artistic forms.
The possibility is endless.
Please refer to the examples attached.

Other than the main focus of the cappuccino art, your can add other elements to make it more appealing and tempting, such as the cappuccino cup, plate, coffee beans, biscuits, etc. Basically these added elements are to give the "Real Feel" of tasting a cappuccino (in this case is mocha flavor) drink.

Create something different. Something extraordinary.

All the best and Good Luck!

Best Regards,
Marcus
+65 9143 6072
Updates

Project Deadline Extended Reason: I HAVE NOT FOUND ANY GOOD DESIGNS THAT IS CLOSE TO MY EXPECTATION.PLEASE DO YOUR BEST TO SUBMIT BETTER DESIGN QUALITY.THANK YOU AND GOOD LUCK!REGARDS,MARCUS Added Monday, March 9, 2015

Project Deadline Extended Reason: I haven't found good designs yet.Please submit more designs with much better quality.Best Regards,Marcus Added Wednesday, April 8, 2015

Project Deadline Extended Reason: I WOULD LIKE TO RECEIVE MUCH BETTER DESIGNS. Added Friday, June 26, 2015

Dear All Designers, I have extended the project deadline as I haven't found a satisfactory design yet. I have also updated the project brief, and narrowed the concept to make a cappuccino art as the main object on my product label. I believe with the provision of this concept, you should be able to create a great design. Thank you, Marcus +65 9143 6072

Industry/Entity Type

Product

Requirements
Must have
• I want the product design to have a cappuccino art.
• The shape/ art could be anything: leafs, animal picture, or other artistic forms.
• The possibility is endless.
• Please refer to the examples attached.

```html
<!DOCTYPE html>
<html lang="en">
<head>
<meta charset="utf-8">
<title>Dunra – Vellor Box Label &amp; Flavour Marks</title>
<link rel="stylesheet" href="https://fonts.googleapis.com/css2?family=Teko:wght@400;500&display=swap">
<style>
  :root {
    --bg-centre: #ffffff;
    --bg-edge: #ebebeb;
    --panel: #f3efe8;
    --panel-shadow: rgba(0,0,0,0.18);
    --gold: #d2a74e;
    --gold-light: #f4dc93;
    --gold-mid: #e2bd6a;
    --gold-dark: #b8893a;
    --strawberry: #e2604a;
    --grape: #8a5fb6;
    --tea: #8cc04a;
    --white: #ffffff;
  }
  * { margin: 0; padding: 0; box-sizing: border-box; }
  html, body { width: 1200px; height: 900px; overflow: hidden; }
  body {
    position: relative;
    background: radial-gradient(ellipse at 55% 45%, var(--bg-centre) 40%, var(--bg-edge) 100%);
    font-family: "Teko", "Arial Narrow", sans-serif;
    color: var(--gold);
  }

  /* Label panels */
  .label-panel {
    position: absolute;
    top: 162px;
    width: 218px;
    height: 544px;
    background: var(--panel);
    box-shadow: 0 1px 3px var(--panel-shadow);
    overflow: hidden;
  }
  .label-panel--back { left: 122px; }
  .label-panel--front { left: 347px; }

  /* Cappuccino latte-art areas (soft gradient placeholders) */
  .latte-art {
    position: absolute;
    left: 0;
    width: 100%;
  }
  .latte-art--top {
    top: 0;
    height: 182px;
    background:
      radial-gradient(circle at 72% 38%, var(--gold-light) 0 8%, var(--gold-mid) 18%, transparent 34%),
      radial-gradient(circle at 20% 22%, var(--gold-light) 0 6%, var(--gold-mid) 16%, transparent 30%),
      radial-gradient(ellipse at 50% 0%, var(--gold-mid), var(--gold) 60%, var(--gold-dark) 100%);
    border-radius: 0 0 62% 38% / 0 0 28% 48%;
  }
  .latte-art--bottom {
    bottom: 0;
    height: 186px;
    background:
      radial-gradient(circle at 28% 58%, var(--gold-light) 0 8%, var(--gold-mid) 20%, transparent 36%),
      radial-gradient(circle at 85% 40%, var(--gold-light) 0 5%, var(--gold-mid) 14%, transparent 28%),
      radial-gradient(ellipse at 50% 100%, var(--gold-mid), var(--gold) 60%, var(--gold-dark) 100%);
    border-radius: 50% 50% 0 0 / 30% 22% 0 0;
  }

  /* Nutrition callout */
  .source-box {
    position: absolute;
    left: 36px;
    top: 214px;
    width: 146px;
    height: 108px;
    border: 2px solid var(--gold);
    text-align: center;
    color: var(--gold);
  }
  .source-box__title {
    height: 22px;
    line-height: 24px;
    font-size: 16px;
    letter-spacing: 1px;
    border-bottom: 2px solid var(--gold);
  }
  .source-box__vitamins {
    height: 42px;
    padding-top: 7px;
    border-bottom: 2px solid var(--gold);
    line-height: 1;
  }
  .source-box__label { font-size: 11px; display: block; }
  .source-box__list { font-size: 14px; letter-spacing: 1px; display: block; margin-top: 2px; }
  .source-box__minerals { font-size: 11px; line-height: 1; padding-top: 7px; }
  .source-box__pointer {
    position: absolute;
    left: 66px;
    bottom: -8px;
    width: 12px;
    height: 12px;
    background: var(--panel);
    border-right: 2px solid var(--gold);
    border-bottom: 2px solid var(--gold);
    transform: rotate(45deg);
  }

  /* Brand name and flavour tag */
  .brand-name {
    font-weight: 500;
    line-height: 1;
    text-align: center;
    letter-spacing: 2px;
  }
  .label-panel--front .brand-name {
    position: absolute;
    left: 0; width: 100%;
    top: 216px;
    font-size: 54px;
    color: var(--gold);
  }
  .flavour-tag {
    border: 2px solid currentColor;
    text-align: center;
    font-size: 13px;
    letter-spacing: 3px;
    line-height: 19px;
  }
  .label-panel--front .flavour-tag {
    position: absolute;
    left: 40px; top: 315px;
    width: 140px; height: 21px;
    color: var(--gold);
  }
  .volume {
    position: absolute;
    left: 0; width: 100%;
    bottom: 10px;
    text-align: center;
    font-size: 15px;
    letter-spacing: 1px;
    color: var(--white);
  }

  /* Brand marks on the right */
  .brand-mark {
    position: absolute;
    text-align: center;
  }
  .brand-mark--hero {
    left: 675px; top: 172px; width: 440px;
  }
  .brand-mark--hero .brand-name {
    font-size: 190px;
    color: var(--gold);
  }
  .brand-mark--variant { width: 180px; }
  .brand-mark--variant .brand-name {
    font-size: 72px;
    color: inherit;
  }
  .brand-mark--variant .flavour-tag {
    display: inline-block;
    width: 122px;
    height: 22px;
    margin-top: 14px;
    font-size: 12px;
  }
  .mark-mocha { left: 687px; top: 474px; color: var(--gold); }
  .mark-strawberry { left: 907px; top: 474px; color: var(--strawberry); }
  .mark-grape { left: 687px; top: 648px; color: var(--grape); }
  .mark-tea { left: 907px; top: 648px; color: var(--tea); }
</style>
</head>
<body>

  <section class="label-panel label-panel--back" aria-label="Back panel">
    <div class="latte-art latte-art--top" role="img" aria-label="Golden cappuccino latte art: swirling milk-foam roses"></div>
    <div class="source-box">
      <div class="source-box__title">SOURCE</div>
      <div class="source-box__vitamins">
        <span class="source-box__label">VITAMIN</span>
        <span class="source-box__list">A. D3. B1. B6. B12.</span>
      </div>
      <div class="source-box__minerals">CALCIUM<br>PHOSPOR</div>
      <span class="source-box__pointer"></span>
    </div>
    <div class="latte-art latte-art--bottom" role="img" aria-label="Golden cappuccino latte art: swirling milk-foam roses"></div>
  </section>

  <section class="label-panel label-panel--front" aria-label="Front panel">
    <div class="latte-art latte-art--top" role="img" aria-label="Golden cappuccino latte art: swirling milk-foam roses"></div>
    <div class="brand-name">DUNRA</div>
    <div class="flavour-tag">MOCHACCHINO</div>
    <div class="latte-art latte-art--bottom" role="img" aria-label="Golden cappuccino latte art: swirling milk-foam roses"></div>
    <div class="volume">300ML</div>
  </section>

  <div class="brand-mark brand-mark--hero">
    <div class="brand-name">DUNRA</div>
  </div>

  <div class="brand-mark brand-mark--variant mark-mocha">
    <div class="brand-name">DUNRA</div>
    <div class="flavour-tag">MOCHACCHINO</div>
  </div>
  <div class="brand-mark brand-mark--variant mark-strawberry">
    <div class="brand-name">DUNRA</div>
    <div class="flavour-tag">STRAWBERRY</div>
  </div>
  <div class="brand-mark brand-mark--variant mark-grape">
    <div class="brand-name">DUNRA</div>
    <div class="flavour-tag">GRAPE-VINE</div>
  </div>
  <div class="brand-mark brand-mark--variant mark-tea">
    <div class="brand-name">DUNRA</div>
    <div class="flavour-tag">GREEN TEA</div>
  </div>

</body>
</html>
```